Dr Fobu smart screen Flyer design

Hi,

Please see attached file as I have done up a very very basic flyer just with the information that will need to be presented.

Please don't go with this as a format I would like, as I have no design skills at all.

I'm looking for something that is basic but professional looking capturing this information.
I would prefer if the symbols were changed so they were all consistent and the colour scheme worked together with the logo.

If you can use the picture of the screen provided as I will replace this once my product has its photoshoot.

Thanks!

```html
<!DOCTYPE html>
<html lang="en">
<head>
<meta charset="utf-8">
<title>Dr Fobu Smart Screen Flyer</title>
<link href="https://fonts.googleapis.com/css2?family=Raleway:wght@400;500;600&display=swap" rel="stylesheet">
<style>
  :root {
    --stage: #4f4f51;
    --charcoal: #404042;
    --paper: #ffffff;
    --divider: #f1f1f1;
    --sky: #27aae1;
    --sun: #fbdf37;
    --sun-text: #fbd900;
    --ink: #2b2b2b;
    --light-text: #f2f2f2;
    --grass: #9cb94a;
    --grass-deep: #6f8a3a;
  }
  * { margin: 0; padding: 0; box-sizing: border-box; }
  html, body {
    width: 849px; height: 1200px; overflow: hidden;
    background: var(--stage);
    font-family: "Raleway", sans-serif;
  }
  .flyer {
    position: absolute; left: 11.5px; top: 65.5px;
    width: 1180px; height: 1527px;
    background: var(--paper);
    transform: scale(0.7); transform-origin: top left;
    overflow: hidden;
  }
  .features-panel {
    position: absolute; left: 43px; top: 0; width: 554px; height: 896px;
    background: var(--charcoal);
  }
  .feature { position: absolute; left: 0; width: 554px; }
  .feature-icon { position: absolute; left: 18px; top: -12px; width: 80px; height: 80px; }
  .feature-title {
    position: absolute; left: 134px; top: 0;
    font-size: 20px; font-weight: 500; letter-spacing: 0.2px; white-space: nowrap;
  }
  .feature-title.blue { color: var(--sky); }
  .feature-title.yellow { color: var(--sun-text); }
  .feature-text {
    position: absolute; left: 134px; top: 36px; width: 402px;
    font-size: 20.5px; line-height: 25.5px; color: var(--light-text);
  }
  .line {
    display: block; white-space: nowrap;
    text-align: justify; text-align-last: justify;
  }
  .line.last { text-align-last: left; }
  .product-photo {
    position: absolute; left: 636px; top: 172px; width: 510px; height: 710px;
    background: linear-gradient(180deg, var(--grass-deep) 0%, var(--grass) 55%, #d9e6b4 80%, var(--paper) 100%);
  }
  .divider { position: absolute; left: 0; width: 1180px; height: 16px; background: var(--divider); }
  .benefits-band {
    position: absolute; left: 0; top: 912px; width: 1180px; height: 320px;
    background: var(--sun);
  }
  .benefit { position: absolute; width: 491px; }
  .benefit svg { position: absolute; left: 0; top: 5px; width: 22px; height: 22px; }
  .benefit p {
    margin-left: 34px; font-size: 24.5px; line-height: 30px; color: var(--ink);
  }
  .contact-panel {
    position: absolute; left: 43px; top: 1248px; width: 554px; height: 279px;
    background: var(--charcoal); color: var(--paper); text-align: center;
  }
  .phone { position: absolute; left: 0; width: 554px; top: 36px; font-size: 37px; font-weight: 400; letter-spacing: 0.5px; }
  .quote-note { position: absolute; left: 0; width: 554px; top: 80px; font-size: 23px; }
  .contact-rule { position: absolute; left: 94px; top: 129px; width: 366px; height: 2px; background: var(--paper); }
  .contact-lines { position: absolute; left: 0; width: 554px; top: 150px; font-size: 25.5px; line-height: 32px; }
  .brand {
    position: absolute; left: 672px; top: 1330px; width: 440px; height: 110px;
    display: flex; align-items: center; justify-content: center; gap: 20px;
  }
  .brand-square { width: 34px; height: 34px; background: var(--sky); }
  .brand-name { font-size: 64px; font-weight: 500; color: var(--ink); letter-spacing: 2px; }
</style>
</head>
<body>
<main class="flyer">
  <section class="features-panel">
    <div class="feature" style="top:184px">
      <svg class="feature-icon" viewBox="0 0 80 80">
        <text x="0" y="60" font-family="Raleway, sans-serif" font-weight="700" font-size="44" fill="#27aae1">4G</text>
        <path d="M54 18 a12 12 0 0 1 10 14 M58 10 a20 20 0 0 1 14 24 M62 2 a28 28 0 0 1 18 34" fill="none" stroke="#27aae1" stroke-width="5" stroke-linecap="round"/>
      </svg>
      <h2 class="feature-title blue">4G CAPABLE</h2>
      <p class="feature-text"><span class="line">Change screen content with a click of the</span><span class="line last">mouse anywhere in the world</span></p>
    </div>
    <div class="feature" style="top:312px">
      <svg class="feature-icon" viewBox="0 0 80 80">
        <path d="M6 34 a46 46 0 0 1 68 0 M18 46 a29 29 0 0 1 44 0" fill="none" stroke="#fbd900" stroke-width="9" stroke-linecap="round"/>
        <circle cx="40" cy="62" r="9" fill="#fbd900"/>
      </svg>
      <h2 class="feature-title yellow">WIFI CAPABLE</h2>
      <p class="feature-text"><span class="line">Change screen content with a PC, tablet</span><span class="line last">or mobile phone an easy to use app</span></p>
    </div>
    <div class="feature" style="top:441px">
      <svg class="feature-icon" viewBox="0 0 80 80" stroke="#27aae1" stroke-width="5" stroke-linecap="round" fill="none">
        <circle cx="40" cy="40" r="12"/>
        <path d="M40 6v10 M40 64v10 M6 40h10 M64 40h10 M16 16l7 7 M57 57l7 7 M64 16l-7 7 M23 57l-7 7"/>
      </svg>
      <h2 class="feature-title blue">INTELIGENT BRIGHTNESS CONTROL</h2>
      <p class="feature-text"><span class="line">Screen will automatically adjust to suit</span><span class="line">ambiant light improving screen viewing</span><span class="line last">quality and saving in power consumption</span></p>
    </div>
    <div class="feature" style="top:594px">
      <svg class="feature-icon" viewBox="0 0 80 80" stroke="#fbd900" stroke-width="3" fill="none" stroke-linecap="round">
        <rect x="12" y="36" width="50" height="30"/>
        <path d="M4 72h72 l-6 6 H10z"/>
        <rect x="42" y="4" width="10" height="40" rx="5"/>
        <circle cx="47" cy="46" r="7" fill="#fbd900"/>
        <path d="M22 8v16 M14 16h16 M16 10l12 12 M28 10l-12 12"/>
      </svg>
      <h2 class="feature-title yellow">ONLINE MONITORING</h2>
      <p class="feature-text"><span class="line">Monitor cabinet temperature and humid-</span><span class="line">ity plus more in real time online. Recieve</span><span class="line last">alerts via email</span></p>
    </div>
    <div class="feature" style="top:748px">
      <svg class="feature-icon" viewBox="0 0 80 80">
        <path d="M30 46h20v32l-10-6-10 6z" fill="#27aae1"/>
        <circle cx="40" cy="28" r="24" fill="#27aae1"/>
        <path d="M40 14l4 9 10 1-7.5 7 2 10-8.5-5-8.5 5 2-10-7.5-7 10-1z" fill="#404042"/>
      </svg>
      <h2 class="feature-title blue">HIGH QUALITY PRODUCTS</h2>
      <p class="feature-text"><span class="line">Setting high standard for colour, bright-</span><span class="line">ness and sharpness these LED modules</span><span class="line last">will create attention</span></p>
    </div>
  </section>

  <div class="product-photo" role="img" aria-label="Product photo of an outdoor LED screen showing a child playing on grass"></div>

  <div class="divider" style="top:896px"></div>
  <section class="benefits-band">
    <div class="benefit" style="left:62px; top:74px">
      <svg viewBox="0 0 22 22"><rect x="2" y="3" width="16" height="16" fill="none" stroke="#2b2b2b" stroke-width="2.5"/><path d="M6 10l4 4 10-11" fill="none" stroke="#2b2b2b" stroke-width="2.5"/></svg>
      <p><span class="line">Bring attnetion to your bussiness with</span><span class="line last">your own hd led display.</span></p>
    </div>
    <div class="benefit" style="left:62px; top:164px">
      <svg viewBox="0 0 22 22"><rect x="2" y="3" width="16" height="16" fill="none" stroke="#2b2b2b" stroke-width="2.5"/><path d="M6 10l4 4 10-11" fill="none" stroke="#2b2b2b" stroke-width="2.5"/></svg>
      <p><span class="line">our displays can be mounted outdoors</span><span class="line">on walls, roofs, xed signs, trailer mount-</span><span class="line last">ed ect.</span></p>
    </div>
    <div class="benefit" style="left:620px; top:74px">
      <svg viewBox="0 0 22 22"><rect x="2" y="3" width="16" height="16" fill="none" stroke="#2b2b2b" stroke-width="2.5"/><path d="M6 10l4 4 10-11" fill="none" stroke="#2b2b2b" stroke-width="2.5"/></svg>
      <p><span class="line">we also do indoor led screens for shop</span><span class="line last">fronts and display stands.</span></p>
    </div>
    <div class="benefit" style="left:620px; top:164px">
      <svg viewBox="0 0 22 22"><rect x="2" y="3" width="16" height="16" fill="none" stroke="#2b2b2b" stroke-width="2.5"/><path d="M6 10l4 4 10-11" fill="none" stroke="#2b2b2b" stroke-width="2.5"/></svg>
      <p><span class="line">All screens are custom built to your re-</span><span class="line">quirements including size, shape and</span><span class="line last">even curved display</span></p>
    </div>
  </section>
  <div class="divider" style="top:1232px"></div>

  <section class="contact-panel">
    <p class="phone">1300 DRFOBUWA</p>
    <p class="quote-note">for a free quote</p>
    <div class="contact-rule"></div>
    <p class="contact-lines">info@drfobuwa.com.au<br>www.drfobuwa.com.au</p>
  </section>

  <div class="brand">
    <span class="brand-square"></span>
    <span class="brand-name">Dr Fobu</span>
  </div>
</main>
</body>
</html>
```